Cedarbrook Residences - Billboard design for our newly renovated townhome community

We have a 5' wide x 4' tall billboard at the entrance to our apartment community, that needs to have the acrylic insert replaced. It is a 2 sided sign, and we are planning to use the same image on both sides. We are called Cedarbrook Residences, and have 48 townhomes that are all 2 bedroom, 1 1/2 bath. A few things we would like to get across on the signage: "Newly Renovated" "2 bed 1 1/2 bath" "Full size W/D in every home" " New Appliances" I've included our parent company's logo - this is the only image I could think of, but it might not be worth having it on the sign. We are in Colorado, so mountain theme could be nice and also sunshine/sun since we are called "Cedarbrook"

Industry/Entity Type

Apartment

Font styles to use
Sans Serif

Requirements
Must have
• Newly Renovated
2 bed 1 1/2 bath
Full size W/D in every home
Virtual Tours available
www.marlowepeaksliving.com
855 - 413 - 9268
Nice to have
• We are located in Colorado - possibly mountain theme? Since our community is called "Cedarbrook Residences" - anything bright with Sun / Sunshine might look really nice as well.

```html
<!DOCTYPE html>
<html lang="en">
<head>
<meta charset="utf-8">
<title>Cedarbrook Residences – Entrance Sign</title>
<link rel="stylesheet" href="https://fonts.googleapis.com/css2?family=Open+Sans:wght@600;700;800&display=swap">
<style>
  :root {
    --page: #ecebe8;
    --white: #ffffff;
    --ink: #1f1a1c;
    --sky-top: #fbf7f5;
    --haze: #e8b7a6;
    --glow: #f3a27a;
    --ember: #e77f5c;
    --dusk: #9d5f75;
    --plum: #4c3457;
    --night: #2f2340;
    --orange: #ff4a06;
    --black: #000000;
    --shadow: rgba(20, 10, 20, 0.85);
  }
  * { margin: 0; padding: 0; box-sizing: border-box; }
  html, body {
    width: 1200px; height: 1200px; overflow: hidden;
    background: var(--page);
    font-family: "Open Sans", Arial, sans-serif;
  }
  .sign {
    position: absolute; left: 0; top: 120px;
    width: 1200px; height: 960px; overflow: hidden;
    background: var(--white);
  }
  .sign__scene {
    position: absolute; inset: 0 0 120px 0;
    background:
      radial-gradient(circle at 79% 25%, rgba(255,255,240,0.95) 0, rgba(255,230,190,0.7) 50px, rgba(255,190,140,0) 220px),
      radial-gradient(ellipse at 15% 95%, var(--night) 0, rgba(60,40,80,0.8) 30%, rgba(60,40,80,0) 65%),
      linear-gradient(180deg, var(--sky-top) 0%, var(--haze) 22%, var(--glow) 42%, var(--ember) 60%, var(--dusk) 82%, var(--plum) 100%);
  }
  .brand {
    position: absolute; top: 178px; left: 0; width: 100%;
    display: flex; justify-content: center; align-items: center; gap: 14px;
    font-weight: 700; font-size: 34px; color: var(--ink);
  }
  .brand__mark {
    width: 18px; height: 18px; border-radius: 50%; background: var(--ink);
  }
  .title {
    position: absolute; top: 270px; left: 0; width: 100%;
    text-align: center; color: var(--white);
    font-weight: 800; line-height: 118px; font-size: 112px;
    letter-spacing: -1px;
    text-shadow: 3px 3px 0 var(--shadow);
  }
  .title span { display: block; }
  .features {
    position: absolute; top: 525px; left: 0; width: 100%;
    list-style: none; text-align: center; color: var(--white);
    font-weight: 600; font-size: 42px; line-height: 59px;
    text-shadow: 2px 2px 2px var(--shadow);
  }
  .contact-bar {
    position: absolute; left: 0; bottom: 0; width: 100%; height: 120px;
    background: var(--orange);
  }
  .contact-bar__phone {
    position: absolute; left: 62px; top: 0; height: 120px;
    display: flex; align-items: center; gap: 18px;
    color: var(--white); font-weight: 700; font-size: 58px; letter-spacing: -1px;
  }
  .contact-bar__web {
    position: absolute; left: 545px; top: 0; right: 0; height: 120px;
    background: var(--black); border-radius: 60px 0 0 60px;
    display: flex; align-items: center; gap: 14px; padding-left: 30px;
    color: var(--white); font-weight: 700; font-size: 33px; white-space: nowrap;
  }
  .icon { flex: none; }
</style>
</head>
<body>
  <main class="sign">
    <div class="sign__scene" role="img" aria-label="Hazy Colorado mountain range at sunrise with a bright sun glowing at the upper right"></div>

    <div class="brand">
      <span class="brand__mark"></span>
      <span class="brand__name">Alder Crest Group</span>
    </div>

    <h1 class="title">
      <span>CEDARBROOK</span>
      <span>RESIDENCES</span>
    </h1>

    <ul class="features">
      <li>Newly Renovated</li>
      <li>New Appliances</li>
      <li>2 bed 1 1/2 bath</li>
      <li>Full size W/D in every home</li>
      <li>Virtual Tours available</li>
    </ul>

    <footer class="contact-bar">
      <div class="contact-bar__phone">
        <svg class="icon" width="46" height="46" viewBox="0 0 24 24" aria-hidden="true">
          <path fill="#fff" d="M6.6 10.8a15.1 15.1 0 0 0 6.6 6.6l2.2-2.2a1 1 0 0 1 1-.25 11.4 11.4 0 0 0 3.6.57 1 1 0 0 1 1 1V20a1 1 0 0 1-1 1A17 17 0 0 1 3 4a1 1 0 0 1 1-1h3.5a1 1 0 0 1 1 1c0 1.25.2 2.45.57 3.57a1 1 0 0 1-.25 1z"/>
          <path fill="none" stroke="#fff" stroke-width="1.8" stroke-linecap="round" d="M14 3.5a6.5 6.5 0 0 1 6.5 6.5M14 7a3 3 0 0 1 3 3"/>
        </svg>
        <span>855-413-9268</span>
      </div>
      <div class="contact-bar__web">
        <svg class="icon" width="38" height="38" viewBox="0 0 42 42" aria-hidden="true">
          <circle cx="21" cy="21" r="19" fill="none" stroke="#fff" stroke-width="2"/>
          <g fill="none" stroke="#fff" stroke-width="1.6">
            <circle cx="21" cy="21" r="11"/>
            <ellipse cx="21" cy="21" rx="5" ry="11"/>
            <line x1="10" y1="21" x2="32" y2="21"/>
            <line x1="12" y1="15.5" x2="30" y2="15.5"/>
            <line x1="12" y1="26.5" x2="30" y2="26.5"/>
          </g>
        </svg>
        <span>www.marlowepeaksliving.com</span>
      </div>
    </footer>
  </main>
</body>
</html>
```